Tranquil Pathways Hypnotherapy Business Card

Logo attached. (will be printing onto thick white/off white textured card)

Double sided business card for two Therapists working at Tranquil Pathways Hypnotherapy.

Require one design, but with different name and mobile numbers on each card.

Target Market(s)

Medical, Health

Industry/Entity Type

Business

Contact Information for Business Card

Need one business card design, but a separate card for each person - Darren Whitfield and Marike de Bruyn.

FRONT OF CARD

Logo

Name (Darren Whitfield on one card, Marike de Bruyn on the other)
Professional Clinical Hypnotherapist

Consulting Rooms (Near Larkmoor Hospital)
284 Bellcrest Avenue
Fernbrook VIC 3188

Darren@TranquilPathwaysHypno.com.au OR Marike@TranquilPathwaysHypno.com.au

Mobile: 0427 862 491 (for Darren) OR
Mobile: 0438 574 206 (for Marike)

BACK OF CARD

Logo

Website: www.TranquilPathwaysHypno.com.au

Phone: 1300 748 519

Requirements
Must have
• Text and logo only. No additiional graphics.

```html
<!DOCTYPE html>
<html lang="en">
<head>
<meta charset="utf-8">
<title>Tranquil Pathways Hypnotherapy – Business Card</title>
<link rel="stylesheet" href="https://fonts.googleapis.com/css2?family=Open+Sans:wght@400;600&family=Montserrat:wght@700&family=Arimo:wght@400&display=swap">
<style>
  :root {
    --navy: #1f2a5c;
    --grey: #6d6e70;
    --ink: #1a1a1a;
    --rule: #7a7a7a;
    --paper: #ffffff;
  }
  html, body {
    margin: 0;
    padding: 0;
    width: 1200px;
    height: 1200px;
    overflow: hidden;
    background: var(--paper);
  }
  .sheet {
    position: relative;
    width: 1200px;
    height: 1200px;
    box-sizing: border-box;
    border: 2px solid var(--ink);
    font-family: "Open Sans", Arial, sans-serif;
    color: var(--ink);
  }
  .card {
    position: absolute;
    left: 245px;
    width: 693px;
    box-sizing: border-box;
    border: 1px solid var(--rule);
    background: var(--paper);
  }
  .card--front { top: 155px; height: 421px; overflow: hidden; }
  .card--back  { top: 621px; height: 418px; }

  /* Front */
  .holder {
    position: absolute;
    left: -75px;
    width: 500px;
    top: 178px;
    text-align: center;
  }
  .holder__name {
    margin: 0;
    font-size: 31px;
    font-weight: 400;
    line-height: 1.1;
    letter-spacing: 0.2px;
  }
  .holder__title {
    margin: 0;
    font-size: 14px;
    line-height: 1.2;
  }
  .divider {
    position: absolute;
    background: var(--ink);
  }
  .card--front .divider { left: 339px; top: 76px; width: 2px; height: 269px; }

  .brand {
    position: absolute;
    display: flex;
    align-items: center;
  }
  .brand__dot {
    flex: none;
    border-radius: 50%;
    background: var(--navy);
  }
  .brand__name {
    margin: 0;
    font-family: "Montserrat", Arial, sans-serif;
    font-weight: 700;
    color: var(--navy);
    line-height: 1.1;
  }
  .brand--small { left: 370px; top: 121px; gap: 12px; }
  .brand--small .brand__dot { width: 62px; height: 62px; }
  .brand--small .brand__name { font-size: 18px; }

  .contact {
    position: absolute;
    left: 367px;
    top: 215px;
    margin: 0;
    font-size: 13px;
    line-height: 19px;
    font-style: normal;
    white-space: nowrap;
  }
  .contact__label { display: inline-block; width: 50px; }

  .band { position: absolute; left: 0; right: 0; }
  .band--grey { top: 394px; height: 7px; background: var(--grey); }
  .band--navy { top: 401px; height: 20px; background: var(--navy); }

  /* Back */
  .card--back .brand--large { left: 125px; top: 139px; gap: 0; }
  .brand--large .brand__dot { width: 138px; height: 138px; }
  .card--back .divider { left: 277px; top: 143px; width: 2px; height: 130px; background: var(--grey); }
  .back-name {
    position: absolute;
    left: 295px;
    top: 167px;
    margin: 0;
    font-family: "Montserrat", Arial, sans-serif;
    font-weight: 700;
    font-size: 30px;
    line-height: 34px;
    color: var(--navy);
    white-space: nowrap;
  }
  .back-details {
    position: absolute;
    left: 285px;
    width: 300px;
    top: 250px;
    margin: 0;
    text-align: center;
    font-family: "Arimo", Arial, sans-serif;
    font-size: 16px;
    line-height: 24px;
    font-style: normal;
    white-space: nowrap;
  }
</style>
</head>
<body>
<main class="sheet">

  <section class="card card--front" aria-label="Card front">
    <div class="holder">
      <h1 class="holder__name">Darren Whitfield</h1>
      <p class="holder__title">Professional Clinical Hypnotherapist</p>
    </div>

    <div class="divider"></div>

    <div class="brand brand--small">
      <span class="brand__dot"></span>
      <p class="brand__name">Tranquil Pathways<br>Hypnotherapy</p>
    </div>

    <address class="contact">
      Consulting Rooms (Near Larkmoor Hospital)<br>
      284 Bellcrest Avenue<br>
      Fernbrook VIC 3188<br>
      <span class="contact__label">Mobile</span>: 0427 862 491<br>
      <span class="contact__label">E-Mail</span>: Darren@TranquilPathwaysHypno.com.au
    </address>

    <div class="band band--grey"></div>
    <div class="band band--navy"></div>
  </section>

  <section class="card card--back" aria-label="Card back">
    <div class="brand brand--large">
      <span class="brand__dot"></span>
    </div>
    <div class="divider"></div>
    <p class="back-name">Tranquil Pathways<br>Hypnotherapy</p>
    <address class="back-details">
      www.TranquilPathwaysHypno.com.au<br>
      Phone: 1300 748 519
    </address>
  </section>

</main>
</body>
</html>
```